Driftwood Coatings of Central Florida, LLC. Start-up painting business needs a professional web desig

We have a start up painting business that would like to reach/focus on commercial clients like building contractors, HOA's, apartment complexes, etc.. We would like a residential aspect to the web design as well. We have an existing website at "trydriftwoodcoatings.com" with usable content. Have logo and color scheme attached. Use provided website ONLY as template. Add commercial services page. Can type own content when needed.

```html
<!DOCTYPE html>
<html lang="en">
<head>
<meta charset="utf-8">
<title>Driftwood Coatings of Central Florida, LLC</title>
<link href="https://fonts.googleapis.com/css2?family=Open+Sans:wght@400;600;700;800&display=swap" rel="stylesheet">
<style>
:root{
  --olive:#6b6843;
  --page:#e7e3dd;
  --card:#ffffff;
  --panel:#f3f1ee;
  --ink:#2b2b2b;
  --text:#555555;
  --icon:#cbb9aa;
  --rule:#c9bfae;
  --accent:#d9897d;
  --seal:#c3c1bd;
}
*{box-sizing:border-box;margin:0;padding:0}
html,body{width:810px;height:1200px;overflow:hidden}
body{background:var(--page);font-family:"Open Sans",Arial,sans-serif;color:var(--text);position:relative}
.topbar{position:absolute;left:0;top:0;width:810px;height:22px;background:var(--olive);color:#fff;font-size:8.5px;display:flex;justify-content:flex-end;align-items:center;gap:18px;padding-right:38px}
.topbar span{display:flex;align-items:center;gap:4px}
.sidebar{position:absolute;left:123px;top:34px;width:108px;height:283px;background:#fff;border-radius:3px;box-shadow:0 1px 3px rgba(0,0,0,.25)}
.brand{height:96px;border-bottom:2px solid #e2ddd5;display:flex;flex-direction:column;align-items:center;justify-content:flex-end;padding-bottom:7px}
.brand-mark{width:26px;height:26px;border-radius:50%;background:var(--accent);margin-bottom:12px}
.brand-name{font-size:7.2px;line-height:1.25;text-align:center;color:var(--ink);text-transform:uppercase}
.nav{list-style:none;padding:12px 12px 0;border-bottom:2px solid #e2ddd5;height:143px}
.nav li{text-align:center;font-size:8px;font-weight:700;color:var(--ink);height:23.5px;line-height:23.5px;border-bottom:1px dashed #d8d2c8}
.nav li:last-child{border-bottom:none}
.nav li.active{background:var(--olive);color:#fff;height:24px;border-bottom:none;margin-bottom:1px}
.social{display:flex;justify-content:center;gap:6px;padding-top:11px}
.social i{width:17px;height:17px;background:#ddd3c8;border-radius:2px;display:block}
.badge{position:absolute;left:137px;top:329px;width:84px;height:84px;border-radius:50%;background:var(--seal)}
.hero{position:absolute;left:243px;top:34px;width:444px;height:228px;background:#fff;border-radius:3px;padding:12px}
.hero-image{position:relative;width:420px;height:204px;background:linear-gradient(100deg,#e9c9a0 0%,#f0dbbd 45%,#d9b58a 100%)}
.hero-caption{position:absolute;left:1px;top:157px;width:206px;height:19px;background:var(--accent);color:#fff;font-weight:700;font-size:12px;line-height:19px;padding-left:5px;white-space:nowrap}
.hero-arrows{position:absolute;left:1px;top:186px;display:flex;gap:2px}
.hero-arrows span{width:17px;height:17px;background:var(--olive);display:flex;align-items:center;justify-content:center}
.main{position:absolute;left:243px;top:274px;width:444px;height:891px;background:var(--panel);border-radius:3px;box-shadow:0 1px 3px rgba(0,0,0,.2)}
.card{position:absolute;background:var(--card);display:flex;flex-direction:column;align-items:center;text-align:center}
.card .icon{margin-top:12px;height:20px}
.card h2{font-weight:800;font-size:16.5px;color:var(--ink);margin-top:4px;letter-spacing:-.2px}
.card .rule{width:38px;border-top:1px dashed var(--rule);margin:9px 0 11px}
.card h3{font-size:9px;font-weight:700;color:var(--ink);line-height:1.35;text-transform:uppercase}
.card p{font-size:8.4px;line-height:1.45;color:var(--text)}
.btn{background:var(--olive);color:#fff;font-size:7.5px;font-weight:700;padding:0 7px;height:18px;line-height:18px;text-transform:uppercase;display:inline-block}
.hours{left:12px;top:12px;width:204px;height:173px}
.hours .day{margin-top:2px}
.hours .time{font-size:8.6px;margin-bottom:11px}
.about{left:12px;top:199px;width:204px;height:354px}
.about h3{padding:0 10px}
.about p{text-align:justify;text-align-last:center;padding:0 11px;margin-top:11px;font-size:8.2px;letter-spacing:-.1px}
.about .btn{margin-top:auto;margin-bottom:13px}
.services{left:12px;top:566px;width:204px;height:312px}
.services-image{width:180px;height:112px;margin-top:17px;background:linear-gradient(180deg,#c83d3d 0%,#d9595a 60%,#2f2a28 100%)}
.services p{padding:0 12px;margin-top:11px}
.services .btn{margin-top:12px}
.portfolio{left:228px;top:12px;width:205px;height:272px}
.thumbs{display:grid;grid-template-columns:84px 84px;gap:12px 12px}
.thumb{width:84px;height:84px}
.t1{background:linear-gradient(135deg,#f2e6c8,#f0b233)}
.t2{background:linear-gradient(135deg,#b83525,#e6e0da)}
.t3{background:linear-gradient(135deg,#8b6cb2,#c9b6df)}
.t4{background:linear-gradient(135deg,#3aa7a8,#6ec5c4)}
.testimonials{left:228px;top:297px;width:205px;height:368px}
.meta{display:flex;gap:7px;font-size:7px;color:var(--ink);margin-top:8px;align-items:center}
.video{width:180px;height:140px;margin-top:12px;background:linear-gradient(90deg,#4b4238 0%,#8a7564 55%,#3a3530 100%)}
.testimonials p{padding:0 14px;margin-top:10px}
.testimonials .btn{margin-top:11px}
.quote{left:228px;top:679px;width:205px;height:199px}
.quote .qmark{margin-top:9px;font-size:30px;line-height:20px;height:20px;font-weight:800;color:var(--icon)}
.field{width:180px;height:18px;border:1px solid #cfcac3;font-size:7.5px;color:#aaa;text-align:left;padding-left:4px;line-height:16px;margin-bottom:9px}
.quote .btn{margin-top:6px;padding:0 14px}
.footer{position:absolute;left:0;top:1175px;width:810px;text-align:center;font-size:7px;color:#fff}
</style>
</head>
<body>
<header class="topbar">
  <span><svg width="7" height="9" viewBox="0 0 7 9"><path d="M3.5 0C1.6 0 0 1.5 0 3.4 0 6 3.5 9 3.5 9S7 6 7 3.4C7 1.5 5.4 0 3.5 0zm0 4.8a1.4 1.4 0 110-2.8 1.4 1.4 0 010 2.8z" fill="#fff"/></svg>1187 Marsh Heron Lane, Lakeland, FL 33801</span>
  <span><svg width="8" height="8" viewBox="0 0 8 8"><path d="M1.6 0l1.3 1.8-.8 1c.5 1 1.2 1.7 2.1 2.1l1-.8L8 5.4 7 7.6C3.5 7.5.5 4.5.4 1z" fill="#fff"/></svg>+1.863-555-0148</span>
</header>

<aside class="sidebar">
  <div class="brand">
    <span class="brand-mark"></span>
    <div class="brand-name">Driftwood Coatings of<br>Central Florida, LLC.</div>
  </div>
  <ul class="nav">
    <li class="active">HOME</li>
    <li>ABOUT US</li>
    <li>SERVICES +</li>
    <li>PORTFOLIO</li>
    <li>CONTACT US</li>
  </ul>
  <div class="social"><i></i><i></i><i></i><i></i></div>
</aside>
<div class="badge" role="img" aria-label="Contractor approval badge"></div>

<section class="hero">
  <div class="hero-image" role="img" aria-label="Warm beige living room with a painted blossom branch mural">
    <div class="hero-caption">WHERE DREAMS MEET REALITY</div>
    <div class="hero-arrows">
      <span><svg width="8" height="8" viewBox="0 0 8 8"><path d="M7 4H1M4 1L1 4l3 3" stroke="#fff" stroke-width="1.4" fill="none"/></svg></span>
      <span><svg width="8" height="8" viewBox="0 0 8 8"><path d="M1 4h6M4 1l3 3-3 3" stroke="#fff" stroke-width="1.4" fill="none"/></svg></span>
    </div>
  </div>
</section>

<main class="main">
  <article class="card hours">
    <svg class="icon" width="20" height="20" viewBox="0 0 20 20"><circle cx="10" cy="10" r="8.5" fill="none" stroke="var(--icon)" stroke-width="2"/><path d="M10 5v5h4" stroke="var(--icon)" stroke-width="2" fill="none"/></svg>
    <h2>HOURS</h2>
    <div class="rule"></div>
    <h3 class="day">MONDAY - FRIDAY</h3>
    <div class="time">6AM - 9PM</div>
    <h3 class="day">SATURDAY / SUNDAY</h3>
    <div class="time">6AM - 1PM</div>
  </article>

  <article class="card about">
    <svg class="icon" width="30" height="20" viewBox="0 0 30 20"><path d="M2 14L15 3l13 11" stroke="var(--icon)" stroke-width="2.2" fill="none"/><rect x="13" y="9" width="4" height="4" fill="var(--icon)"/></svg>
    <h2>ABOUT US</h2>
    <div class="rule"></div>
    <h3>The best home painters are yours<br>for the taking</h3>
    <p>Driftwood Coatings of Central Florida, LLC. has painted thousands of homes in its day, but the one we're most excited about painting is the one we're painting today. Your home could be that home.</p>
    <p>Know what you want? Great. We love to execute on a homeowner's vision. Not sure whether to go mild or wild? That's where our consultative approach and vast experience shines. We'll come up with a concept that you'll love, and then we'll make it happen.</p>
    <p>Call today to schedule your appointment and free estimate. We can't wait to hear from you!</p>
    <span class="btn">READ MORE</span>
  </article>

  <article class="card services">
    <svg class="icon" width="22" height="22" viewBox="0 0 22 22"><path d="M14 2l6 6-7 7-6-6z" fill="none" stroke="var(--icon)" stroke-width="2"/><path d="M8 12l-5 7 2 1 6-6" fill="var(--icon)"/></svg>
    <h2>SERVICES</h2>
    <div class="rule"></div>
    <h3>Commercial Services</h3>
    <div class="services-image" role="img" aria-label="Crew on scaffolding painting a red commercial building"></div>
    <p>Lorem ipsum dolor sit amet, consectetur adipisicing elit, sed do eiusmod tempor incididunt ut labore et dolore magna aliqua.</p>
    <span class="btn">VIEW ALL</span>
  </article>

  <article class="card portfolio">
    <svg class="icon" width="22" height="20" viewBox="0 0 22 20"><rect x="1" y="5" width="20" height="14" rx="2" fill="var(--icon)"/><rect x="7" y="2" width="8" height="4" fill="var(--icon)"/><circle cx="11" cy="12" r="4" fill="#fff"/><circle cx="11" cy="12" r="2.3" fill="var(--icon)"/></svg>
    <h2>PORTFOLIO</h2>
    <div class="rule"></div>
    <div class="thumbs">
      <div class="thumb t1" role="img" aria-label="Yellow and white painted living room"></div>
      <div class="thumb t2" role="img" aria-label="Red accent wall with shelving"></div>
      <div class="thumb t3" role="img" aria-label="Purple painted bedroom"></div>
      <div class="thumb t4" role="img" aria-label="Teal painted dining area"></div>
    </div>
  </article>

  <article class="card testimonials">
    <svg class="icon" width="20" height="20" viewBox="0 0 20 20"><path d="M3 17l1-5L14 2l4 4L8 16z" fill="var(--icon)"/><path d="M3 17l5-1" stroke="#fff" stroke-width="1"/></svg>
    <h2>TESTIMONIALS</h2>
    <div class="rule"></div>
    <h3>Best thing we<br>ever did...</h3>
    <div class="meta">
      <span>&#9638; JUN 01, 2015</span><span>&#9670; REVIEW</span><span>&#9679; 3</span>
    </div>
    <div class="video" role="img" aria-label="Customer testimonial video"></div>
    <p>Lorem ipsum dolor sit amet, consectetur adipisicing elit, sed do eiusmod tempor incididunt ut labore et dolore magna aliqua.</p>
    <span class="btn">READ MORE</span>
  </article>

  <article class="card quote">
    <div class="qmark">&rdquo;</div>
    <h2>GET A FREE QUOTE</h2>
    <div class="rule"></div>
    <div class="field">Name*</div>
    <div class="field">Phone*</div>
    <div class="field">Email*</div>
    <span class="btn">SUBMIT</span>
  </article>
</main>

<footer class="footer">&copy; 2015 Driftwood Coatings. All Rights Reserved.</footer>
</body>
</html>
```